Easter. Company for collection, treatment and recovery of dangerous and dangerous goods. not dangerous

We need an image folder with 4 pages, details see insert, logo can not be changed and some pictures collection and treatment of hazardous and non-hazardous waste, Tankwageninnenreinigung own fleet

Target Market(s)

existing customers and new customers

Colors

Designer to choose colors to be used in the design.

Requirements
Must have
• BRAV logo
Nice to have
• Design the text and the pictures so that it suits our disposal company. You can also use the pictures from our webside.

```html
<!DOCTYPE html>
<html lang="de">
<head>
<meta charset="utf-8">
<title>BRAV Imagefolder</title>
<link href="https://fonts.googleapis.com/css2?family=Open+Sans:wght@400;600;700;800&display=swap" rel="stylesheet">
<style>
:root{
  --green:#2f7a4a;
  --green-dark:#1f5b36;
  --green-light:#4f9a62;
  --ink:#3d4a43;
  --grey:#6b6f6d;
  --paper:#ffffff;
  --paper-shade:#eef0ef;
  --backdrop:#e4e6e5;
}
*{margin:0;padding:0;box-sizing:border-box}
html,body{width:898px;height:1200px;overflow:hidden;background:var(--backdrop);font-family:"Open Sans",Arial,sans-serif;color:var(--ink)}
.canvas{position:relative;width:898px;height:1200px}
.page{position:absolute;background:linear-gradient(180deg,var(--paper) 0%,var(--paper-shade) 100%);overflow:hidden;box-shadow:0 2px 8px rgba(0,0,0,.18)}
.spread{position:absolute;left:29px;top:20px;width:840px;height:565px;box-shadow:0 2px 8px rgba(0,0,0,.18);overflow:hidden;background:linear-gradient(180deg,var(--paper),var(--paper-shade))}
.spread .fold{position:absolute;left:419px;top:0;width:2px;height:100%;background:rgba(0,0,0,.06)}
.spread svg.cover-art{position:absolute;left:0;top:0}
.brand{font-weight:800;color:var(--green);letter-spacing:1px;line-height:1;display:flex;align-items:center;gap:6px}
.brand .dot{width:9px;height:9px;border-radius:50%;background:var(--green)}
.abs{position:absolute;z-index:1}
.intro{left:24px;top:22px;width:260px;font-size:6.6px;line-height:1.5;color:var(--grey)}
.intro p+p{margin-top:5px}
.back-brand{left:32px;top:170px;font-size:22px}
.contact{left:32px;top:440px;font-size:7.5px;color:var(--grey);line-height:1.7}
.contact h3{font-size:13px;font-weight:600;color:var(--green);letter-spacing:.3px;margin-bottom:3px}
.contact li{list-style:none;display:flex;align-items:center;gap:6px}
.contact svg{flex:none}
.emergency-line{left:250px;top:515px;font-size:8.5px;color:var(--ink)}
.emergency-line b{color:var(--green-dark)}
.badges{left:300px;top:478px;display:flex;gap:10px}
.badge{width:22px;height:22px;border-radius:50%;background:#c9cfcb}
.badge.sq{border-radius:3px;background:#b6c5ba}
.front-brand{left:630px;top:40px;font-size:26px}
.claim{left:450px;top:430px;width:370px}
.claim h2{font-size:9px;font-weight:700;color:var(--green-dark);line-height:1.35;text-transform:uppercase}
.claim ul{list-style:none;display:grid;grid-template-columns:1fr 1fr;gap:2px 10px;margin-top:8px;font-size:7.2px;color:var(--grey)}
.claim li::before{content:"› ";color:var(--green);font-weight:700}
.claim .web{margin-top:10px;text-align:right;font-size:8px;font-weight:700;color:var(--ink)}
.page-title{font-size:15px;font-weight:600;color:var(--grey);line-height:1.2}
.cols{display:grid;grid-template-columns:1fr 1fr;gap:14px}
.col h4{font-size:9.4px;font-weight:600;color:var(--green-dark);line-height:1.2;margin-bottom:5px;text-transform:uppercase}
.col h4+ul+h4{margin-top:12px}
.ticks{list-style:none;font-size:6.4px;line-height:1.45;color:var(--ink)}
.ticks>li{position:relative;padding-left:10px;margin-bottom:3px}
.ticks>li::before{content:"";position:absolute;left:1px;top:2px;width:4px;height:2.5px;border-left:1.2px solid var(--ink);border-bottom:1.2px solid var(--ink);transform:rotate(-45deg)}
.ticks small{display:block;font-size:5.6px;color:var(--grey)}
.footer-band{position:absolute;left:0;bottom:0;width:100%;height:30px;background:linear-gradient(180deg,var(--green-light),var(--green-dark));color:#fff;font-size:13px;display:flex;align-items:center;justify-content:center;gap:5px;border-top:3px solid #d7e4da}
.footer-band b{font-weight:700}
.body-text{font-size:6.4px;line-height:1.45;color:var(--ink);text-align:justify}
.body-text b{font-weight:700}
.section-head{font-size:13px;font-weight:600;color:var(--green-dark);text-transform:uppercase}
.section-head span{font-weight:800;font-size:15px}
.photo{border-radius:2px}
</style>
</head>
<body>
<main class="canvas">

  <!-- Outer cover spread: back cover (left) and front cover (right) -->
  <section class="spread" aria-label="Umschlag außen">
    <svg class="cover-art" width="840" height="565" viewBox="0 0 840 565">
      <defs>
        <linearGradient id="terraceTone" x1="0" y1="0" x2="1" y2="1">
          <stop offset="0" stop-color="#7d94a8"/>
          <stop offset=".35" stop-color="#6f8a4c"/>
          <stop offset=".7" stop-color="#8fa35a"/>
          <stop offset="1" stop-color="#5a6a3a"/>
        </linearGradient>
        <linearGradient id="siteTone" x1="0" y1="0" x2="0" y2="1">
          <stop offset="0" stop-color="#a9c3da"/>
          <stop offset="1" stop-color="#6f7d86"/>
        </linearGradient>
        <linearGradient id="swooshTone" x1="0" y1="0" x2="1" y2="1">
          <stop offset="0" stop-color="#4f9a62"/>
          <stop offset="1" stop-color="#1f5b36"/>
        </linearGradient>
      </defs>
      <ellipse cx="430" cy="268" rx="325" ry="118" transform="rotate(-15 430 268)" fill="url(#swooshTone)"/>
      <ellipse cx="450" cy="256" rx="310" ry="110" transform="rotate(-15 450 256)" fill="#fff"/>
      <ellipse cx="460" cy="252" rx="295" ry="102" transform="rotate(-15 460 252)" fill="url(#terraceTone)" role="img" aria-label="Foto: grüne Reisterrassen im Gegenlicht"/>
      <circle cx="305" cy="155" r="44" fill="url(#siteTone)" stroke="#fff" stroke-width="4" role="img" aria-label="Foto: Betriebsgelände aus der Luft"/>
      <circle cx="640" cy="290" r="44" fill="url(#siteTone)" stroke="#fff" stroke-width="4" role="img" aria-label="Foto: Tankwagen vor der Halle"/>
    </svg>
    <div class="fold"></div>

    <div class="abs intro">
      <p>BRAV Umweltschutz und Wertstoff-Recycling ist ein modernes, mittelständisches Dienstleistungsunternehmen im Zentralraum Oberösterreichs, das mit zeitgemäßer Verfahrenstechnik eine Vielzahl an Lösungen für Entsorgung und Recycling anbietet.</p>
      <p>BRAV ist seit 1976 am Standort tätig.</p>
      <p>With our certifications and memberships we underline our position as a leading disposal specialist.</p>
    </div>
    <div class="abs brand back-brand"><span class="dot"></span>BRAV</div>

    <div class="abs contact">
      <h3>GET IN TOUCH WITH US</h3>
      <ul>
        <li><svg width="7" height="9" viewBox="0 0 7 9"><path d="M3.5 0a3.5 3.5 0 0 0-3.5 3.5C0 6 3.5 9 3.5 9S7 6 7 3.5A3.5 3.5 0 0 0 3.5 0z" fill="#6b6f6d"/><circle cx="3.5" cy="3.5" r="1.2" fill="#fff"/></svg>Lindenweg 14, 4600 Wels</li>
        <li><svg width="8" height="8" viewBox="0 0 8 8"><path d="M1.6 0l1.5 2-1 1a5 5 0 0 0 2.9 2.9l1-1 2 1.5L7 8A7 7 0 0 1 0 1z" fill="#6b6f6d"/></svg>0043/7242/31870</li>
        <li><svg width="8" height="8" viewBox="0 0 8 8"><rect x="0" y="2" width="8" height="5" rx="1" fill="#6b6f6d"/></svg>0043/7242/31871</li>
        <li><svg width="8" height="6" viewBox="0 0 8 6"><rect width="8" height="6" rx="1" fill="#6b6f6d"/><path d="M0 0l4 3 4-3" stroke="#fff" fill="none"/></svg>office@brav-umwelt.at</li>
        <li><svg width="8" height="6" viewBox="0 0 8 6"><rect width="8" height="6" rx="1" fill="#6b6f6d"/><path d="M0 0l4 3 4-3" stroke="#fff" fill="none"/></svg>tank@brav-umwelt.at</li>
        <li><svg width="8" height="8" viewBox="0 0 8 8"><circle cx="4" cy="4" r="4" fill="#6b6f6d"/></svg>www.brav-umwelt.at</li>
      </ul>
    </div>
    <div class="abs badges"><span class="badge sq"></span><span class="badge"></span><span class="badge"></span></div>
    <div class="abs emergency-line">24h Notdienst: <b>0664/52 70 31 19</b></div>

    <div class="abs brand front-brand"><span class="dot"></span>BRAV</div>
    <div class="abs claim">
      <h2>Qualität, Umwelt, Sicherheit und Gesundheitsschutz<br>sind wichtige Bestandteile des Managementsystems der BRAV.</h2>
      <ul>
        <li>Abfallsammlung</li>
        <li>Abfallentsorgung</li>
        <li>Abfallbehandlung</li>
        <li>Tankwageninnenreinigung</li>
        <li>Reinigung von Industrieanlagen und Behälter</li>
      </ul>
      <p class="web">www.brav-umwelt.at</p>
    </div>
  </section>

  <!-- Inside left: services -->
  <section class="page" style="left:20px;top:612px;width:420px;height:568px" aria-label="Innenseite Dienstleistungen">
    <h1 class="abs page-title" style="left:16px;top:16px">UNSERE DIENSTLEISTUNGEN<br>UND SCHWERPUNKTE</h1>
    <svg class="abs" style="left:0;top:48px;z-index:0" width="420" height="270" viewBox="0 0 420 270">
      <defs>
        <linearGradient id="forestTone" x1="0" y1="0" x2="1" y2="1">
          <stop offset="0" stop-color="#3f5a2a"/>
          <stop offset=".5" stop-color="#b9c46a"/>
          <stop offset="1" stop-color="#4d6b2c"/>
        </linearGradient>
        <linearGradient id="swooshTone2" x1="0" y1="0" x2="1" y2="1">
          <stop offset="0" stop-color="#4f9a62"/>
          <stop offset="1" stop-color="#1f5b36"/>
        </linearGradient>
      </defs>
      <ellipse cx="245" cy="135" rx="245" ry="118" transform="rotate(-10 245 135)" fill="url(#swooshTone2)"/>
      <ellipse cx="262" cy="126" rx="222" ry="106" transform="rotate(-10 262 126)" fill="#fff"/>
      <ellipse cx="272" cy="122" rx="205" ry="98" transform="rotate(-10 272 122)" fill="url(#forestTone)" role="img" aria-label="Foto: lichtdurchfluteter Nadelwald"/>
      <circle cx="98" cy="228" r="40" fill="#fff"/>
    </svg>
    <div class="abs brand" style="left:66px;top:268px;font-size:17px"><span class="dot"></span>BRAV</div>

    <div class="abs cols" style="left:16px;top:330px;width:392px">
      <div class="col">
        <h4>Entsorgungsdienstleistungen<br>und Abfallmanagement</h4>
        <ul class="ticks">
          <li>Sammlung - Behandlung- Verwertung von Abfällen
            <small>• gefährlicher und nicht gefährlicher</small>
            <small>• in flüssiger, fester und pastöser Form</small></li>
          <li>Entleerung und Reinigung von:
            <small>• Rohr-, Kanal- und Tankanlagen</small>
            <small>• Gruben und Sickerschächten</small>
            <small>• Öl- und Fettabscheidern</small></li>
          <li>Reinigung von Industrieanlagen und Behältersystemen</li>
          <li>Abwasser- und Abfallanalytik</li>
          <li>TV - Kanalinspektion</li>
          <li>Sanierung von Altlasten</li>
          <li>Behälter- und Containerservice / Sicherheitsfässer Tankwageninnenreinigung</li>
        </ul>
      </div>
      <div class="col">
        <h4>Tankwageninnenreinigung</h4>
        <ul class="ticks">
          <li>Lebensmittel Produkte</li>
          <li>Chemische Produkte<small>(Begriff für nicht Lebensmittelprodukte)</small></li>
          <li>Alle Klassen außer 1,2,7</li>
          <li>Reinigung von Fässern und Behältern</li>
        </ul>
        <h4>Standorte, Anlagen und<br>Kompetenzen</h4>
        <ul class="ticks">
          <li>Standorte in Wels und Asten</li>
          <li>CPB-Chemisch-physikalisch-biologische Anlage zur Behandlung von Abfällen</li>
          <li>Tankwagenreinigungsanlage mit 4 Bahnen</li>
          <li>Fuhrpark zur Sammlung &amp; Transport von Abfällen<small>(Tochterfirma HELMER)</small></li>
          <li>Umfangreicher Genehmigungskatalog zur Sammlung und Verwertung von gefährlichen und nicht gefährlichen Abfällen <small style="display:inline">(1200 Abfallarten)</small></li>
        </ul>
      </div>
    </div>
    <div class="footer-band">24h Notdienst: <b>0664/52 70 31 19</b></div>
  </section>

  <!-- Inside right: tank cleaning and treatment plant -->
  <section class="page" style="left:458px;top:612px;width:420px;height:568px" aria-label="Innenseite Tankwagenreinigung">
    <svg class="abs" style="left:0;top:0;z-index:0" width="420" height="290" viewBox="0 0 420 290">
      <defs>
        <linearGradient id="truckTone" x1="0" y1="0" x2="1" y2="1">
          <stop offset="0" stop-color="#2e4a3e"/>
          <stop offset=".45" stop-color="#3f8a5a"/>
          <stop offset=".7" stop-color="#c9b441"/>
          <stop offset="1" stop-color="#2a2f33"/>
        </linearGradient>
        <linearGradient id="swooshTone3" x1="0" y1="0" x2="1" y2="1">
          <stop offset="0" stop-color="#4f9a62"/>
          <stop offset="1" stop-color="#1f5b36"/>
        </linearGradient>
      </defs>
      <ellipse cx="260" cy="150" rx="265" ry="122" transform="rotate(-8 260 150)" fill="url(#swooshTone3)"/>
      <ellipse cx="275" cy="140" rx="245" ry="110" transform="rotate(-8 275 140)" fill="#fff"/>
      <ellipse cx="285" cy="136" rx="230" ry="102" transform="rotate(-8 285 136)" fill="url(#truckTone)" role="img" aria-label="Foto: grüner Tanklastzug in der Reinigungshalle"/>
    </svg>
    <div class="abs brand" style="left:14px;top:16px;font-size:19px"><span class="dot"></span>BRAV</div>
    <h2 class="abs" style="right:16px;top:44px;font-size:14px;font-weight:700;color:#fff;letter-spacing:.2px">TANKWAGENREINIGUNG</h2>

    <div class="abs cols" style="left:12px;top:290px;width:396px;gap:12px">
      <div>
        <p class="body-text"><b>Einer der ersten Tankwageninnenreinigungsanlagen in Österreich, seit 1995 am Standort in Wels, Lindenweg 14.</b> Mit 4 Reinigungsbahnen, 15 Waschköpfe, Dampf, Trocknungsanlage, Verpflegung und Dusche für die LKW-Fahrer.</p>
        <p class="body-text" style="margin-top:6px">Reinigung einer umfangreichen Produktpalete inkl. spezieller Problemprodukte.</p>
        <p class="body-text" style="margin-top:8px">EXTRAS unter <b style="font-size:7.5px">www.brav-umwelt.at</b></p>
      </div>
      <div>
        <p class="body-text">Die Anlage arbeitet nach den Bestimmungen der ETRV (Europäischer Tankreinigungsverband) bzw. ECIR (Europäischer Chemie-Industrierat) und ist QSAS-zertifiziert. Die erfolgte Reinigung bestätigen wir Ihnen mit dem ERD (Europäisches Reinigungsdokument).</p>
        <p class="body-text" style="margin-top:8px">Kontakt: <b style="font-size:7.5px">tank@brav-umwelt.at</b></p>
      </div>
    </div>

    <h3 class="abs section-head" style="left:32px;top:392px"><span>CPB</span> – Chemisch-physikalisch-biologische Anlage</h3>
    <svg class="abs photo" style="left:12px;top:416px" width="190" height="108" viewBox="0 0 190 108">
      <defs>
        <linearGradient id="plantTone" x1="0" y1="0" x2="1" y2="1">
          <stop offset="0" stop-color="#4e6a2a"/>
          <stop offset=".5" stop-color="#a8bf3a"/>
          <stop offset="1" stop-color="#3a5a6a"/>
        </linearGradient>
      </defs>
      <rect width="190" height="108" fill="url(#plantTone)" role="img" aria-label="Foto: Rohrleitungen und Behälter der Behandlungsanlage"/>
    </svg>
    <div class="abs" style="left:214px;top:416px;width:194px">
      <p class="body-text">Unsere CPB-Anlage stellt österreichweit einen einzigartigen Standard dar und wurde vom Österreichischen Umweltbundesamt als führende österreichische Referenzanlage innerhalb der EU, gültig für die IPPC-Richtlinie 2007 (dh die Richtlinie über die integrierte Vermeidung und Verminderung der Umweltverschmutzung) als EU-Standard gelistet. Technisches UNIKAT (Bodenabdichtungen!!)</p>
      <p class="body-text" style="margin-top:6px">Durch die zentrale Lage und eine mögliche Jahreskapazität von ca. 95.000 tonnen sind wir in der Lage, die Gesamtmenge der in Oberösterreich anfallenden spezifischen Abfälle umweltgerecht zu behandeln.</p>
    </div>
    <div class="footer-band">24h Notdienst: <b>0664/52 70 31 19</b></div>
  </section>

</main>
</body>
</html>
```